Brindlecove (main name) sharpening systems(underneath)

Specializing in Knife, Scissors and Clipper sharpening, repair and maintenance.
I would like a logo designed that has at least one of the elements above showing what could happen as a result of the instrument being sharpened by my company as part of the logo (maybe the word Brindlecove being cut in half)

Target Market(s)

commercial (restaurants or any establishment that deals with food preparation, salons, barbershops) residential (any homes that use knives scissors or clippers)

Contact Information for Business Card

Name: Marcus Pellingham
Address: K240 Coral Vista Heights
Cell: 12465917362
Email: brindlecovehone@mailtrove.net

Requirements
Must have
• Brindlecove....sharpening systems clean front with strong logo indicating what we do as part of logo front of card
• Contact details: back of card
• we sharpen on site or pick up and drop off within 24hrs (at back of Card)
• telephone number: (at back) for contact
• address and other details (at back)

```html
<!DOCTYPE html>
<html lang="en">
<head>
<meta charset="utf-8">
<title>Brindlecove Sharpening Systems – Business Card</title>
<link rel="stylesheet" href="https://fonts.googleapis.com/css2?family=Roboto:wght@400;500;700&display=swap">
<style>
  :root {
    --backdrop: #e4e4e4;
    --card-top: #053b6e;
    --card-bottom: #07335f;
    --ink: #ffffff;
    --ink-soft: #e6ecf3;
  }
  * { box-sizing: border-box; margin: 0; padding: 0; }
  html, body {
    width: 1200px; height: 576px; overflow: hidden;
    background: var(--backdrop);
    font-family: "Roboto", Arial, sans-serif;
  }
  .canvas { position: relative; width: 1200px; height: 576px; }
  .card {
    position: absolute;
    width: 482px; height: 291px;
    border-radius: 6px;
    background: linear-gradient(180deg, var(--card-top) 0%, var(--card-bottom) 100%);
    color: var(--ink);
  }
  .card--front { left: 82px; top: 139px; }
  .card--back { left: 602px; top: 138px; }

  .brand { position: absolute; text-align: left; line-height: 1; }
  .brand__name { display: block; font-weight: 700; letter-spacing: -0.5px; }
  .brand__tagline { display: block; font-weight: 700; letter-spacing: 0.3px; }

  .card--front .brand { left: 0; right: 0; top: 112px; text-align: center; }
  .card--front .brand__name { font-size: 46px; }
  .card--front .brand__tagline { font-size: 16px; margin-top: 4px; }

  .card--back .brand { right: 32px; top: 44px; text-align: right; }
  .card--back .brand__name { font-size: 33px; }
  .card--back .brand__tagline { font-size: 11.5px; margin-top: 3px; }

  .holder { position: absolute; left: 28px; top: 44px; }
  .holder__name { font-size: 19px; font-weight: 700; letter-spacing: 0.3px; line-height: 1.1; }
  .holder__title { font-size: 11.5px; font-weight: 400; color: var(--ink-soft); margin-top: 3px; }

  .service {
    position: absolute; left: 28px; top: 140px; width: 300px;
    font-size: 12px; font-weight: 500; line-height: 1.4; color: var(--ink-soft);
  }

  .contact { position: absolute; left: 28px; top: 193px; list-style: none; }
  .contact__item {
    display: flex; align-items: center;
    height: 17.5px; font-size: 12.8px; color: var(--ink-soft);
  }
  .contact__icon { width: 12px; height: 12px; margin-right: 10px; fill: var(--ink); }
  .contact__item--address { margin-top: 3px; }
</style>
</head>
<body>
<main class="canvas">
  <section class="card card--front" aria-label="Card front">
    <div class="brand">
      <span class="brand__name">Brindlecove</span>
      <span class="brand__tagline">sharpening systems</span>
    </div>
  </section>

  <section class="card card--back" aria-label="Card back">
    <div class="holder">
      <p class="holder__name">Marcus Pellingham</p>
      <p class="holder__title">Managing Director</p>
    </div>

    <div class="brand">
      <span class="brand__name">Brindlecove</span>
      <span class="brand__tagline">sharpening systems</span>
    </div>

    <p class="service">We sharpen on site or pick up and drop off within 24hrs</p>

    <ul class="contact">
      <li class="contact__item">
        <svg class="contact__icon" viewBox="0 0 12 12" aria-hidden="true"><path d="M3 0h6a1 1 0 0 1 1 1v10a1 1 0 0 1-1 1H3a1 1 0 0 1-1-1V1a1 1 0 0 1 1-1zm0.4 1.4v8h5.2v-8zM6 10.1a.6.6 0 1 0 0 1.2.6.6 0 0 0 0-1.2z"/></svg>
        +1 246 591 7362
      </li>
      <li class="contact__item">
        <svg class="contact__icon" viewBox="0 0 12 12" aria-hidden="true"><path d="M0 4c0-1.5 2.5-2.6 6-2.6S12 2.5 12 4v1H9V3.8H3V5H0zM2.5 6h7l1.5 5H1zM6 7.2a1.5 1.5 0 1 0 0 3 1.5 1.5 0 0 0 0-3z"/></svg>
        www.brindlecovesharp.net
      </li>
      <li class="contact__item">
        <svg class="contact__icon" viewBox="0 0 12 12" aria-hidden="true"><path d="M0 2.5h12v7H0zM1 3.3l5 3.6 5-3.6v-.1H1z"/></svg>
        brindlecovehone@mailtrove.net
      </li>
      <li class="contact__item contact__item--address">K240 Coral Vista Heights</li>
    </ul>
  </section>
</main>
</body>
</html>
```